Brightacre - online store for farm produce

Online store selling fresh produce (vegetables, fruits, dairy products, meat, ...) from various farmers. Every farm has its own shopping window - order page - just like a really simple web store.

Please check the attached design brief and mock-ups for further details.

Target Market(s)

People looking for fresh vegetables, fruit, meat, ... delivered from farms

Industry/Entity Type

Farming

Coding

Coded - Design and coding required

Number of Pages Required

5+ page

Font styles to use
Sans Serif

Requirements
Must have
• Custom design. Good UX/UI design, very functional.
Responsive using bootstrap 12 point grid system

```html
<!DOCTYPE html>
<html lang="en">
<head>
<meta charset="utf-8">
<title>Brightacre – Online Store</title>
<link href="https://fonts.googleapis.com/css2?family=Caveat+Brush&family=Raleway:wght@400;500;600;700&display=swap" rel="stylesheet">
<style>
  :root{
    --red:#ec1c24;
    --ink:#222222;
    --text:#4a4a4a;
    --nav:#232323;
    --grey-light:#f6f6f6;
    --grey-mid:#efeeef;
    --btn:#333333;
    --btn-shadow:#8a8a8a;
    --lime:#8fd10f;
    --white:#ffffff;
  }
  *{box-sizing:border-box;margin:0;padding:0}
  html,body{width:1200px;height:3042px;overflow:hidden;background:var(--white)}
  body{position:relative;font-family:'Raleway',sans-serif;color:var(--text)}
  .abs{position:absolute}
  .hand{font-family:'Caveat Brush',cursive;color:var(--red);letter-spacing:1.5px;text-transform:uppercase}

  /* nav */
  .site-nav{left:0;top:0;width:1200px;height:67px;background:var(--nav)}
  .brand{left:153px;top:12px;font-family:'Raleway',sans-serif;font-weight:600;font-size:28px;color:var(--red)}
  .nav-link{top:20px;font-size:17px;color:#e6e6e6}
  .btn-login{left:842px;top:11px;width:112px;height:41px;background:var(--red);color:#fff;font-size:14px;font-weight:700;display:flex;align-items:center;justify-content:center;gap:6px}
  .btn-logout{left:978px;top:22px;font-size:14px;font-weight:700;color:#fff}

  /* hero */
  .hero{left:0;top:67px;width:1200px;height:571px;background:radial-gradient(ellipse at 60% 40%,#6b3b5a 0%,#3d5a22 35%,#2a3a18 60%,#1c2412 100%)}
  .hero-edge{left:0;top:600px;width:1200px;height:60px}
  .hero-title{left:0;top:270px;width:1200px;text-align:center;font-family:'Caveat Brush',cursive;color:#fff;font-size:56px;line-height:58px;letter-spacing:2px}
  .hero-title span{color:var(--red)}
  .dots{left:580px;top:557px;display:flex;gap:6px}
  .dots i{width:11px;height:11px;border-radius:50%;border:1.5px solid #fff;display:block}
  .dots i.on{background:var(--red);border-color:var(--red)}

  /* shared */
  .section-title{font-size:38px;line-height:40px}
  .body-copy{font-size:17px;line-height:22px}
  .btn{display:flex;align-items:center;justify-content:center;background:var(--btn);color:#fff;font-weight:700;font-size:16px;box-shadow:8px 7px 0 var(--btn-shadow)}
  .bullets{list-style:none}
  .bullets li{position:relative;padding-left:38px;font-size:17.5px;height:33px;line-height:22px}
  .bullets li::before{content:"";position:absolute;left:0;top:6px;width:9px;height:9px;border-radius:50%;background:#8c8c8c}

  /* about */
  .about-photo{left:603px;top:729px;width:437px;height:334px;background:linear-gradient(135deg,#d86a1e 0%,#7c3b6a 40%,#4d7a2a 70%,#c9b21c 100%)}
  .about-frame{left:624px;top:716px;width:406px;height:362px;border:3px solid var(--red)}
  .about-deco{left:0;top:945px;width:200px;height:236px;background:radial-gradient(circle at 30% 50%,#7a8a3a 0%,#c9a62a 45%,rgba(255,255,255,0) 75%)}

  .band-farmer{left:0;top:1181px;width:1200px;height:481px;background:var(--grey-light)}
  .farmer-photo{left:603px;top:1181px;width:448px;height:448px;border-radius:50%;background:radial-gradient(circle at 50% 45%,#f0a24a 0%,#c9875a 30%,#5a4a40 65%,#2a2a2a 100%)}

  .band-customer{left:0;top:1662px;width:1200px;height:509px;background:var(--grey-mid)}
  .customer-photo{left:130px;top:1689px;width:448px;height:448px;border-radius:50%;background:radial-gradient(circle at 50% 45%,#e9e4df 0%,#b99a8a 35%,#6e7a4a 70%,#3e3e4a 100%)}
  .potatoes{left:980px;top:1937px;width:220px;height:234px;background:radial-gradient(ellipse at 60% 40%,#d7a862 0%,#b7884a 45%,rgba(239,238,239,0) 78%)}

  /* featured */
  .featured{left:0;top:2171px;width:1200px;height:533px;background:linear-gradient(180deg,#f7f6f7 0%,#e2e4e2 40%,#8ea36c 70%,#3f5a22 92%,#141a0c 100%)}
  .featured-title{left:0;top:2248px;width:1200px;text-align:center}
  .featured-copy{left:230px;top:2316px;width:740px;text-align:center;color:#333}

  /* footer */
  .footer{left:0;top:2704px;width:1200px;height:338px;background:#060606}
  .footer-foliage{left:0;top:2930px;width:1200px;height:112px;background:linear-gradient(90deg,#3d6a1a 0%,#1f3a10 20%,#0a0a0a 40%,#0a0a0a 60%,#2a4a14 80%,#6a8a2a 100%)}
  .social{top:2731px;width:36px;height:36px;border-radius:50%}
  .phone{left:0;top:2784px;width:1200px;text-align:center;color:#fff;font-size:26px;display:flex;justify-content:center;align-items:center;gap:6px}
  .address{left:0;top:2820px;width:1200px;text-align:center;color:#fff;font-size:16px;display:flex;justify-content:center;align-items:center;gap:12px}
  .footer-links{left:0;top:2862px;width:1200px;text-align:center;color:#fff;font-size:17px;word-spacing:2px}
  .footer-links b{font-weight:400;margin:0 14px}
  .copyright{left:0;top:2895px;width:1200px;text-align:center;color:#fff;font-size:13px}
  .copyright span{color:var(--red)}
  .cookie-bar{left:154px;top:2924px;width:881px;height:111px;background:var(--lime)}
  .cookie-copy{left:178px;top:2939px;width:600px;font-size:14.5px;line-height:20px;color:#222}
  .cookie-copy a{color:var(--red);font-weight:700;text-decoration:underline}
  .btn-ok{left:882px;top:2944px;width:128px;height:46px;background:var(--red);color:#fff;font-weight:700;font-size:17px;display:flex;align-items:center;justify-content:center;box-shadow:6px 6px 0 #fff}
</style>
</head>
<body>

<header class="abs site-nav">
</header>
<div class="abs brand">Brightacre</div>
<a class="abs nav-link" style="left:422px">Current offer</a>
<a class="abs nav-link" style="left:554px">Farm directory</a>
<a class="abs nav-link" style="left:710px">Settings</a>
<div class="abs btn-login">
  <svg width="14" height="16" viewBox="0 0 14 16" fill="none" stroke="#fff" stroke-width="1.6"><rect x="4" y="1" width="9" height="14"/><path d="M1 8h7M5 5l3 3-3 3"/></svg>
  LOG IN
</div>
<div class="abs btn-logout">LOG OUT</div>

<section class="abs hero" role="img" aria-label="Overhead photo of fresh vegetables: cabbage, pumpkin, carrots, lettuce and peppers"></section>
<svg class="abs hero-edge" viewBox="0 0 1200 60" preserveAspectRatio="none"><path d="M0 20 Q150 38 300 26 T600 30 T900 24 T1200 38 V60 H0Z" fill="#fff"/></svg>
<h1 class="abs hero-title">Online <span>Store</span><br>Selling fresh produce</h1>
<div class="abs dots"><i class="on"></i><i></i><i></i></div>

<!-- about -->
<div class="abs about-deco" role="img" aria-label="Vegetables spilling in from the left edge"></div>
<h2 class="abs hand section-title" style="left:151px;top:742px">What is this about</h2>
<p class="abs body-copy" style="left:151px;top:794px;width:370px">He point of using Lorem Ipsum is that it has a more-or-less normal distribution of letters, as opposed to using 'Content here, content here', making it look like readable English. Many desktop publishing packages and web page editors now use Lorem Ipsum as their default model text, and a search for 'lorem ipsum' will</p>
<div class="abs btn" style="left:152px;top:992px;width:147px;height:53px">Product Search</div>
<div class="abs about-photo" role="img" aria-label="Photo of mixed fresh vegetables"></div>
<div class="abs about-frame"></div>

<!-- farmer -->
<div class="abs band-farmer"></div>
<h2 class="abs hand section-title" style="left:151px;top:1258px">Benefits for the farmer</h2>
<ul class="abs bullets" style="left:152px;top:1315px">
  <li>He point of using Lorem Ipsum</li>
  <li>More-or-less normal distribution of letters,</li>
  <li>Editors now use Lorem Ipsum as their</li>
  <li>Default model text, and a search</li>
  <li>Uncover many web sites still in their infancy.</li>
  <li>He point of using Lorem Ipsum</li>
</ul>
<div class="abs btn" style="left:152px;top:1522px;width:147px;height:53px">Tell Me More</div>
<div class="abs farmer-photo" role="img" aria-label="Two farmers shaking hands against a sunset, in a paint-splash shape"></div>

<!-- customer -->
<div class="abs band-customer"></div>
<div class="abs customer-photo" role="img" aria-label="Smiling customer buying vegetables at a market stall, in a paint-splash shape"></div>
<h2 class="abs hand section-title" style="left:605px;top:1754px">Benefits for the customer</h2>
<ul class="abs bullets" style="left:605px;top:1810px">
  <li>He point of using Lorem Ipsum</li>
  <li>More-or-less normal distribution of letters,</li>
  <li>Editors now use Lorem Ipsum as their</li>
  <li>Default model text, and a search</li>
  <li>Uncover many web sites still in their infancy.</li>
  <li>More-or-less normal distribution of letters,</li>
</ul>
<div class="abs btn" style="left:605px;top:2023px;width:147px;height:53px">Search Product</div>
<div class="abs potatoes" role="img" aria-label="Potatoes in a burlap sack"></div>

<!-- featured -->
<section class="abs featured" role="img" aria-label="Greenhouse interior with rows of young green crops"></section>
<h2 class="abs hand section-title featured-title">Featured product / farm</h2>
<p class="abs body-copy featured-copy">Lorem ipsum dolor sit amet, consectetur adipiscing elit. Etiam blandit ipsum quis viverra vehicula. Duis sit amet posuere neque, eu malesuada risus. Vivamus pharetra sodales accumsan. Aenean eu enim malesuada, pretium lectus id, molestie lacus. Sed quis mauris non quam dapibus pellentesque. Fusce feugiat blandit vehicula. Integer ut consequat nisl. Morbi vel ornare ipsum. Proin a neque at enim scelerisque imperdiet a eu diam. Aliquam neque dui, fringilla in orci a, commodo accumsan odio.</p>
<div class="abs btn" style="left:518px;top:2458px;width:148px;height:54px;box-shadow:8px 7px 0 #fff">Link to Farm</div>

<!-- footer -->
<footer class="abs footer"></footer>
<div class="abs footer-foliage" role="img" aria-label="Fresh leafy greens and vegetables along the bottom edge"></div>
<div class="abs social" style="left:503px;background:#1da1f2"></div>
<div class="abs social" style="left:555px;background:#e0452f"></div>
<div class="abs social" style="left:608px;background:#3b5998"></div>
<div class="abs social" style="left:660px;background:#d6366e"></div>
<div class="abs phone">
  <svg width="14" height="18" viewBox="0 0 14 18" fill="none" stroke="#fff" stroke-width="1.6"><path d="M4 1 L1 3 Q0 9 5 15 Q7 17 9 17 L11 14 L8 11 L6 12 Q4 9 4 6 L6 5Z"/></svg>
  555-010-2048
</div>
<div class="abs address">
  <svg width="11" height="15" viewBox="0 0 11 15"><path d="M5.5 0A5.5 5.5 0 0 0 0 5.5C0 9.5 5.5 15 5.5 15S11 9.5 11 5.5A5.5 5.5 0 0 0 5.5 0Z" fill="#fff"/><circle cx="5.5" cy="5.5" r="2" fill="#060606"/></svg>
  Lorem Ipsum,UK
</div>
<div class="abs footer-links">Terms &amp; Condition<b>I</b>Cookies Policies<b>I</b>Contact</div>
<div class="abs copyright">Copyright©<span>brightacre</span> .All Rights Reserved.</div>

<div class="abs cookie-bar"></div>
<p class="abs cookie-copy">Lorem Ipsum is simply dummy text of the printing and typesetting industry. Lorem Ipsum has been the industry's standard dummy text ever since typesetting industry. Lorem Ipsum has been the industry's standard dummy <a>Cookies policy page</a></p>
<div class="abs btn-ok">OK</div>

</body>
</html>
```